Professional/modern business card design for construction company

We need a new business card design, double sided keeping it modern, sleek, professional and simple. We are an earthmoving business but do not want any pictures of machinery. I would like one side to have the logo and the other to have all the information, keeping with the colors in our logo. The business card will need to be able to be customised so we can use it for several different managers., we would also like to be able to use the design to apply it to other stationary ie. letterheads, notebooks etc. We do not really have a tag line but we could put on there that we specialise in - Agriculture, Civil Construction and Mining.

Contact Information for Business Card

Brolga Ridge Excavations Pty Ltd
ABN 58 402 937 615
82 Gumleaf Creek Road, Moree NSW 2400

Harold Benton
Managing Director
P 0418 639 204
E haroldbenton@brolgaridgeexc.com.au

Font styles to use
Serif
Sans Serif

Requirements
Nice to have
• I have attached some examples of ideas.
Should not have
• images of machinery

```html
<!DOCTYPE html>
<html lang="en">
<head>
<meta charset="utf-8">
<title>Brolga Ridge Excavations – Stationery</title>
<link rel="stylesheet" href="https://fonts.googleapis.com/css2?family=Montserrat:wght@700&family=Questrial&family=Arimo:wght@400&display=swap">
<style>
  :root {
    --orange: #f38a21;
    --charcoal: #444444;
    --paper: #ffffff;
    --backdrop: #e3e3df;
    --ink: #111111;
    --faint: #efefef;
  }
  * { box-sizing: border-box; margin: 0; padding: 0; }
  html, body { width: 1200px; height: 960px; overflow: hidden; }
  body { position: relative; background: var(--backdrop); font-family: "Arimo", Arial, sans-serif; }

  .piece { position: absolute; background: var(--paper); overflow: hidden; }
  .piece > svg.shapes { position: absolute; inset: 0; width: 100%; height: 100%; }

  .brand { position: absolute; display: flex; align-items: center; gap: 6px; }
  .brand-square { background: var(--orange); flex: none; }
  .brand-name {
    font-family: "Montserrat", Arial, sans-serif; font-weight: 700;
    color: var(--charcoal); text-transform: uppercase; line-height: 1.1;
  }
  .brand-name span { display: block; }

  .identity { position: absolute; left: 898px; top: 32px; width: 200px; }
  .identity .brand { position: static; gap: 10px; }
  .identity .brand-square { width: 30px; height: 30px; }
  .identity .brand-name { font-size: 19px; letter-spacing: .5px; }
  .identity .brand-name .sub { font-size: 11px; letter-spacing: .4px; }
  .tagline {
    margin-top: 34px; font-family: "Questrial", Arial, sans-serif;
    font-size: 11.5px; color: var(--ink); white-space: nowrap;
  }

  .letterhead { left: 140px; top: 109px; width: 366px; height: 525px; }
  .letterhead .brand { left: 29px; top: 40px; }
  .letterhead .brand-square { width: 14px; height: 14px; }
  .letterhead .brand-name { font-size: 9px; }
  .letterhead .brand-name .sub { font-size: 5.5px; }
  .letter-body {
    position: absolute; left: 45px; top: 157px; width: 277px;
    font-size: 7.2px; line-height: 9.5px; text-align: justify; color: var(--ink);
  }
  .letter-watermark {
    position: absolute; left: 98px; top: 250px;
    font-family: "Montserrat", Arial, sans-serif; font-weight: 700;
    font-size: 16px; color: var(--faint); text-transform: uppercase; line-height: 1.1;
  }
  .signature-mark {
    position: absolute; left: 185px; top: 299px; width: 110px; height: 16px;
    background: linear-gradient(90deg, #dfe3ee, #c9cfe0);
  }
  .signature-line {
    position: absolute; left: 173px; top: 319px; width: 145px;
    border-top: 1px solid var(--ink);
  }
  .signature-label {
    position: absolute; left: 173px; top: 321px; width: 119px;
    text-align: center; font-size: 7px; color: var(--ink);
  }
  .letter-footer {
    position: absolute; left: 0; bottom: 0; width: 100%; height: 40px;
    background: var(--charcoal); padding: 6px 0 0 19px;
  }
  .contact-lines {
    font-family: "Questrial", Arial, sans-serif; font-size: 5.6px; line-height: 8px;
  }
  .letter-footer .contact-lines { color: var(--orange); }

  .notebook { left: 655px; top: 169px; width: 298px; height: 405px; background: #f4f4f4; }
  .notebook .brand { left: 147px; top: 282px; }
  .notebook .brand-square { width: 20px; height: 20px; }
  .notebook .brand-name { font-size: 12px; }
  .notebook .brand-name .sub { font-size: 7.5px; }

  .card { left: 140px; top: 713px; width: 382px; height: 167px; }
  .card .brand { left: 32px; top: 63px; }
  .card .brand-square { width: 20px; height: 20px; }
  .card .brand-name { font-size: 12px; }
  .card .brand-name .sub { font-size: 7.5px; }
  .card-details {
    position: absolute; left: 214px; top: 56px; width: 160px;
    font-family: "Questrial", Arial, sans-serif; color: var(--charcoal);
    font-size: 7.6px; line-height: 11px; white-space: nowrap;
  }
  .card-details .person {
    font-family: "Montserrat", Arial, sans-serif; font-weight: 700;
    font-size: 10px; line-height: 12px; color: var(--charcoal);
  }
  .card-details .role { color: var(--orange); margin-bottom: 4px; }
  .card-details .key { color: var(--orange); font-weight: 700; margin-right: 3px; }

  .envelope { left: 600px; top: 706px; width: 382px; height: 167px; }
  .envelope .contact-lines { position: absolute; left: 35px; top: 110px; color: var(--charcoal); }
  .envelope .brand { left: 236px; top: 93px; }
  .envelope .brand-square { width: 18px; height: 18px; }
  .envelope .brand-name { font-size: 10.5px; }
  .envelope .brand-name .sub { font-size: 7px; }
  .envelope-band {
    position: absolute; left: 0; bottom: 0; width: 100%; height: 12px; background: var(--charcoal);
  }
</style>
</head>
<body>

  <header class="identity">
    <div class="brand">
      <div class="brand-square"></div>
      <div class="brand-name"><span>Brolga Ridge</span><span class="sub">Excavations Pty Ltd</span></div>
    </div>
    <p class="tagline">Agriculture, Civil Construction and Mining.</p>
  </header>

  <section class="piece letterhead">
    <svg class="shapes" viewBox="0 0 366 525" preserveAspectRatio="none">
      <polygon points="0,0 366,0 366,60" fill="var(--orange)"/>
    </svg>
    <div class="brand">
      <div class="brand-square"></div>
      <div class="brand-name"><span>Brolga Ridge</span><span class="sub">Excavations Pty Ltd</span></div>
    </div>
    <div class="letter-watermark"><span>Brolga Ridge</span><br><span>Excavations Pty Ltd</span></div>
    <p class="letter-body">It is a long established fact that a reader will be distracted by the readable content of a page when looking at its layout. The point of using Lorem Ipsum is that it has a more-or-less normal distribution of letters, as opposed to using 'Content here, content here', making it look like readable English. Many desktop publishing packages and web page editors now use Lorem Ipsum as their default model text, and a search for 'lorem ipsum' will uncover many web sites still in their infancy. Various versions have evolved over the years, sometimes by accident, sometimes on purpose (injected humour and the like).</p>
    <div class="signature-mark" role="img" aria-label="Handwritten signature of Harold Benton"></div>
    <div class="signature-line"></div>
    <p class="signature-label">Signature</p>
    <footer class="letter-footer">
      <p class="contact-lines">Brolga Ridge Excavations Pty Ltd<br>ABN 58 402 937 615<br>82 Gumleaf Creek Road, Moree NSW 2400</p>
    </footer>
  </section>

  <section class="piece notebook">
    <svg class="shapes" viewBox="0 0 298 405" preserveAspectRatio="none">
      <polygon points="0,0 298,0 298,102" fill="var(--orange)"/>
      <polygon points="0,308 298,405 0,405" fill="var(--charcoal)"/>
    </svg>
    <div class="brand">
      <div class="brand-square"></div>
      <div class="brand-name"><span>Brolga Ridge</span><span class="sub">Excavations Pty Ltd</span></div>
    </div>
  </section>

  <section class="piece card">
    <svg class="shapes" viewBox="0 0 382 167" preserveAspectRatio="none">
      <polygon points="0,0 382,0 382,40" fill="var(--orange)"/>
      <polygon points="0,127 382,167 0,167" fill="var(--charcoal)"/>
    </svg>
    <div class="brand">
      <div class="brand-square"></div>
      <div class="brand-name"><span>Brolga Ridge</span><span class="sub">Excavations Pty Ltd</span></div>
    </div>
    <div class="card-details">
      <p class="person">Harold Benton</p>
      <p class="role">Managing Director</p>
      <p><span class="key">P</span>0418 639 204</p>
      <p><span class="key">E</span>haroldbenton@brolgaridgeexc.com.au</p>
    </div>
  </section>

  <section class="piece envelope">
    <svg class="shapes" viewBox="0 0 382 167" preserveAspectRatio="none">
      <path d="M0,0 H382 V4 L370,40 Q362,58 340,58 H42 Q20,58 12,40 L0,4 Z" fill="var(--orange)"/>
    </svg>
    <p class="contact-lines">Brolga Ridge Excavations Pty Ltd<br>ABN 58 402 937 615<br>82 Gumleaf Creek Road, Moree NSW 2400</p>
    <div class="brand">
      <div class="brand-square"></div>
      <div class="brand-name"><span>Brolga Ridge</span><span class="sub">Excavations Pty Ltd</span></div>
    </div>
    <div class="envelope-band"></div>
  </section>

</body>
</html>
```